Velora Company website for beauty pre & post natal products

i need to have a company website for my new start up company Velora. Velora means woman in latin. My website url is www.velora-mums.example, i have no contents yet. Velora is focus on selling pre and post natal beauty products e.g.: maternity belt, post natal girdles, maternity bra, etc.. products that beautify woman before and after maternity. I would like the website to potray beauty and yet confident woman. i have attached the sample of the product.
Updates

hi creative designers, I'm looking for your creativity that best to portray my company website, a local company based in Singapore that focus on selling beauty pre and post natal products to beautify motherhood and all women out there

Target Market(s)

Women (age 24-40), mother, career woman, etc

Industry/Entity Type

It Company

Number of Pages Required

5+ page

Font styles to use
Serif
Sans Serif

Requirements
Must have
• - Home page
• (highlights of products, company, beauty elegant women with small children, etc)
• - About Us
• Velora is founded in 2015 in Singapore by a proud mommy of 2 sons. During maternity period which before and after pregnancy, it is extremely crucial for woman to give extra care for herself and her body from the effect of pregnancy due to physical and hormonal changes.
• - Products
• - Client's testimonials
• - Contact Us
• - Inquiry Form
Nice to have
• Professional, yet elegant and appealing to women nowadays. It should show level of trust and credibility just from entering the website.
Should not have
• BIG NO to dark colors, gloomy colors or animations.

```html
<!DOCTYPE html>
<html lang="en">
<head>
<meta charset="utf-8">
<title>Velora — Pre &amp; Post Natal Beauty</title>
<link href="https://fonts.googleapis.com/css2?family=Lato:wght@300;400;700&display=swap" rel="stylesheet">
<style>
  :root {
    --red: #d60000;
    --deep-red: #990000;
    --title-red: #a00000;
    --sub-red: #c80000;
    --pink: #ff8fb0;
    --white: #ffffff;
    --heading-dark: #330000;
    --body-grey: #7a7a7a;
    --photo-a: #f3e2dc;
    --photo-b: #e9d6cf;
    --product-a: #9ea4a2;
    --product-b: #c9c7c3;
  }
  * { margin: 0; padding: 0; box-sizing: border-box; }
  html, body { width: 1200px; height: 1000px; overflow: hidden; background: var(--white); }
  body { font-family: 'Lato', sans-serif; position: relative; }

  .site-header { position: absolute; top: 0; left: 0; width: 1200px; height: 70px; background: var(--red); }
  .header-accent { position: absolute; top: 0; left: 0; }
  .brand { position: absolute; left: 132px; top: 20px; font-size: 28px; font-weight: 400; color: var(--pink); letter-spacing: 1px; line-height: 1; }
  .main-nav { position: absolute; top: 28px; right: 0; display: flex; }
  .main-nav a { position: absolute; color: var(--white); text-decoration: none; font-size: 16px; white-space: nowrap; top: 0; }

  .hero { position: absolute; top: 70px; left: 0; width: 1200px; height: 346px; background: var(--white); }
  .hero-photo { position: absolute; left: 140px; top: 0; width: 470px; height: 346px; background: linear-gradient(90deg, var(--photo-a), var(--photo-b) 55%, #f7eeea); }
  .hero-arrow { position: absolute; top: 148px; }
  .hero-arrow.prev { left: 44px; }
  .hero-arrow.next { left: 1143px; }
  .hero-copy { position: absolute; left: 604px; width: 500px; top: 122px; text-align: center; }
  .hero-title { font-size: 31px; font-weight: 700; color: var(--title-red); line-height: 1.1; }
  .hero-subtitle { font-size: 22px; font-weight: 400; color: var(--sub-red); line-height: 1.1; margin-top: 2px; }
  .hero-button { display: inline-block; margin-top: 21px; width: 159px; height: 35px; border: 2px solid var(--title-red); border-radius: 5px; color: var(--title-red); font-size: 16px; line-height: 31px; text-decoration: none; }

  .products { position: absolute; top: 416px; left: 0; width: 1200px; height: 300px; background: var(--deep-red); }
  .section-label { position: absolute; left: 128px; top: 22px; font-size: 20px; font-weight: 400; color: var(--white); }
  .product-card { position: absolute; top: 58px; width: 192px; height: 192px; border-radius: 50%; background: var(--white); box-shadow: 0 9px 0 #6a0000; }
  .product-card .product-photo { position: absolute; inset: 7px; border-radius: 50%; background: linear-gradient(180deg, var(--product-a) 0%, var(--product-b) 60%, #e4e4e6 100%); display: flex; align-items: center; justify-content: center; }
  .product-name { font-size: 15px; font-weight: 700; color: var(--white); }

  .about { position: absolute; top: 716px; left: 0; width: 1200px; height: 284px; }
  .about-heading { position: absolute; left: 131px; top: 25px; font-size: 20px; font-weight: 400; color: var(--heading-dark); }
  .about-text { position: absolute; left: 240px; width: 742px; top: 97px; text-align: center; font-size: 21px; font-weight: 300; line-height: 26.5px; color: var(--body-grey); }
  .about-text strong { font-weight: 700; }
</style>
</head>
<body>
  <header class="site-header">
    <svg class="header-accent" width="320" height="70" viewBox="0 0 320 70" aria-hidden="true">
      <polygon points="0,0 243,0 295,70 0,70" fill="#990000"/>
      <polygon points="243,0 262,0 314,70 295,70" fill="#ffffff"/>
    </svg>
    <div class="brand">Velora</div>
    <nav class="main-nav">
      <a href="#" style="left:-725px">ABOUT</a>
      <a href="#" style="left:-642px">PRODUCTS</a>
      <a href="#" style="left:-529px">CLIENT’S&nbsp; TESTIMONIALS</a>
      <a href="#" style="left:-318px">INQUIRY FORM</a>
      <a href="#" style="left:-173px">CONTACT</a>
    </nav>
  </header>

  <section class="hero">
    <div class="hero-photo" role="img" aria-label="Photo of a pregnant woman and a slim post-natal figure in white underwear"></div>
    <svg class="hero-arrow prev" width="18" height="64" viewBox="0 0 18 64" aria-hidden="true">
      <polyline points="16,1 2,32 16,63" fill="none" stroke="#a00000" stroke-width="2"/>
    </svg>
    <svg class="hero-arrow next" width="18" height="64" viewBox="0 0 18 64" aria-hidden="true">
      <polyline points="2,1 16,32 2,63" fill="none" stroke="#a00000" stroke-width="2"/>
    </svg>
    <div class="hero-copy">
      <h1 class="hero-title">Post-Natal &amp; Slimming Girdle</h1>
      <p class="hero-subtitle">INNER &amp; OUTER BENGKUNG</p>
      <a href="#" class="hero-button">LEARN MORE</a>
    </div>
  </section>

  <section class="products">
    <h2 class="section-label">PRODUCTS</h2>
    <div class="product-card" style="left:226px">
      <div class="product-photo" role="img" aria-label="Product photo of an inner bengkung girdle worn on the torso"><span class="product-name">INNER BENGKUNG</span></div>
    </div>
    <div class="product-card" style="left:510px">
      <div class="product-photo" role="img" aria-label="Product photo of an inner bengkung girdle worn on the torso"><span class="product-name">INNER BENGKUNG</span></div>
    </div>
    <div class="product-card" style="left:792px">
      <div class="product-photo" role="img" aria-label="Product photo of an inner bengkung girdle worn on the torso"><span class="product-name">INNER BENGKUNG</span></div>
    </div>
  </section>

  <section class="about">
    <h2 class="about-heading">ABOUT US</h2>
    <p class="about-text"><strong>Velora</strong> is founded in 2015 in Singapore by a proud mommy of 2 sons. During maternity period which before and after pregnancy, it is extremely crucial for woman to give extra care for herself and her body from the effect of pregnancy due to physical and hormonal changes.</p>
  </section>
</body>
</html>
```